ONE PAGE WEBSITE for Brisk Talent Agency

Hello creative gurus,

We're are after a ONE PAGE World Press web design.

We're a recruitment start-up specializing in Information Technology.

The design should be cool, quirky and NOT mainstream.

The kind of web designs we like:

http://www.quvantrix.co.za/#what-we-do
http://foldamarble.com/
http://www.kelzo.com/index.html#home
http://marcellotavoni.com/#/selected-works

And, we only like the front page of this web site: http://www.dunvelpath.com/

Any questions, please do let us know!

Thank you, and happy creating!

Rudi

Reason: Just need a day or two to finalize everything. Thanks, Rudi

Target Market(s)

Companies, employees, candidates

Industry/Entity Type

Recruitment

Coding

Coded - Design and coding required

Colors
f37122
f68e4e
ffcf3e
00a990
86cfc6
fcca95
fee18a

Requirements
Must have
• 1. The website should be techy, cool, funky, quirky and user-friendly.
• 2. Mobile-compatible
• 3. Please use our spaceman logo through the website (attached).
• 4. Please see attached website content/brief.
• 5. Colors - orange color is a must, but please use other colors to spice it up - make it more fun.
• The kind of web designs we like:
• http://www.quvantrix.co.za/#what-we-do
• http://foldamarble.com/
• http://www.kelzo.com/index.html#home
• http://marcellotavoni.com/#/selected-works
• http://www.dunvelpath.com/
• Any questions, please do let us know!
Should not have
• -NO stock image banners, photos, images

```html
<!DOCTYPE html>
<html lang="en">
<head>
<meta charset="utf-8">
<title>Brisk Talent</title>
<link rel="stylesheet" href="https://fonts.googleapis.com/css2?family=Montserrat:wght@400;500;600&family=Open+Sans:wght@400;600&family=Quicksand:wght@500&display=swap">
<style>
  :root {
    --orange: #ff6d00;
    --orange-text: #f36a12;
    --ink: #111111;
    --body: #3d3d3d;
    --nav: #5a5a5a;
    --rule: #cfcfcf;
    --footer: #2b2b2b;
    --white: #ffffff;
    --hero-light: #f3f7fa;
    --hero-mid: #dfe6ee;
    --hero-deep: #9aa0c4;
  }
  * { margin: 0; padding: 0; box-sizing: border-box; }
  html, body { width: 1200px; height: 785px; overflow: hidden; background: var(--white); }
  .page { position: relative; width: 1200px; height: 785px; font-family: "Open Sans", sans-serif; color: var(--body); }

  .hero-visual {
    position: absolute; left: 663px; top: 0; width: 537px; height: 468px;
    background:
      radial-gradient(ellipse at 60% 55%, rgba(154,160,196,0.45), rgba(154,160,196,0) 60%),
      linear-gradient(90deg, var(--white) 0%, var(--hero-light) 25%, var(--hero-mid) 70%, var(--hero-light) 100%);
  }

  .brand { position: absolute; left: 103px; top: 17px; display: flex; align-items: center; gap: 8px; }
  .brand-mark { width: 72px; height: 72px; border-radius: 50%; background: #222222; }
  .brand-name { font-family: "Montserrat", sans-serif; font-weight: 600; font-size: 30px; letter-spacing: 2px; color: var(--ink); margin-top: 26px; }

  .main-nav { position: absolute; left: 96px; top: 154px; width: 207px; list-style: none; }
  .main-nav li { height: 40px; border-bottom: 1px solid var(--rule); padding-left: 23px; line-height: 40px;
    font-family: "Montserrat", sans-serif; font-size: 16px; color: var(--nav); }
  .main-nav li:last-child { border-bottom: none; }
  .main-nav li.active { color: var(--orange-text); }

  .intro { position: absolute; left: 364px; top: 158px; width: 380px; }
  .intro-kicker { font-family: "Montserrat", sans-serif; font-weight: 600; font-size: 24px; color: var(--ink); line-height: 28px; }
  .intro-title { font-family: "Montserrat", sans-serif; font-weight: 600; font-size: 32px; color: var(--orange-text); line-height: 38px; margin-top: 4px; }
  .intro p { font-size: 14px; line-height: 21px; margin-top: 22px; }
  .intro p + p { margin-top: 22px; }
  .read-more { display: inline-block; margin-top: 20px; width: 117px; height: 36px; line-height: 36px; text-align: center;
    background: linear-gradient(#3b3b3b, #1c1c1c); color: var(--white); font-family: "Open Sans", sans-serif; font-weight: 600; font-size: 12px; border-radius: 3px; }

  .why { position: absolute; left: 103px; top: 467px; width: 994px; height: 233px; background: var(--orange); color: var(--white); }
  .why-title { position: absolute; left: 42px; top: 29px; font-family: "Quicksand", sans-serif; font-weight: 500; font-size: 26px; }
  .why-point { position: absolute; top: 82px; display: flex; gap: 9px; font-size: 13px; line-height: 21px; }
  .why-point svg { flex: none; margin-top: 3px; }
  .why-point.one { left: 29px; width: 330px; }
  .why-point.two { left: 378px; width: 280px; }
  .why-point.three { left: 692px; width: 270px; }
  .why-call { position: absolute; left: 0; right: 0; top: 199px; text-align: center; font-size: 14px; font-weight: 600; }

  .site-footer { position: absolute; left: 0; top: 715px; width: 1200px; height: 70px; background: var(--footer); color: var(--white); }
  .legal { position: absolute; left: 114px; top: 25px; font-size: 14px; }
  .social { position: absolute; left: 921px; top: 26px; display: flex; gap: 30px; list-style: none; }
  .social li { width: 18px; height: 18px; border-radius: 50%; background: var(--white); }
</style>
</head>
<body>
<div class="page">
  <div class="hero-visual" role="img" aria-label="Silhouettes of business people standing in a bright glass office"></div>

  <header class="brand">
    <div class="brand-mark"></div>
    <span class="brand-name">BRISK</span>
  </header>

  <ul class="main-nav">
    <li class="active">HOME</li>
    <li>COMPANIES</li>
    <li>TALENT</li>
    <li>REFERALS</li>
    <li>ABOUT US</li>
    <li>BLOG</li>
    <li>CONTACT US</li>
  </ul>

  <section class="intro">
    <h2 class="intro-kicker">WELCOME TO</h2>
    <h1 class="intro-title">BRISK TALENT</h1>
    <p>We’re Sydney’s IT talent specialists. We are passionate, with boundless energy, and work to bring great people together.</p>
    <p>We specialise in permanent and contract recruitment solutions across Information Technology.</p>
    <a class="read-more">READ MORE</a>
  </section>

  <section class="why">
    <h2 class="why-title">Why work with us?</h2>
    <div class="why-point one">
      <svg width="22" height="22" viewBox="0 0 22 22"><circle cx="11" cy="11" r="11" fill="#fff"/><path d="M6 11.5l3.5 3.5L16 8" fill="none" stroke="#ff6d00" stroke-width="2.6" stroke-linecap="round" stroke-linejoin="round"/></svg>
      <span>We’re experts in our field and have years of hands-on experience in the I.T. industry. We know our market intimately and understand the unique skills required to build a successful I.T. team</span>
    </div>
    <div class="why-point two">
      <svg width="22" height="22" viewBox="0 0 22 22"><circle cx="11" cy="11" r="11" fill="#fff"/><path d="M6 11.5l3.5 3.5L16 8" fill="none" stroke="#ff6d00" stroke-width="2.6" stroke-linecap="round" stroke-linejoin="round"/></svg>
      <span>We offer a bespoke service with dedicated account manager (a nice one!) who will stay in regular contact with you</span>
    </div>
    <div class="why-point three">
      <svg width="22" height="22" viewBox="0 0 22 22"><circle cx="11" cy="11" r="11" fill="#fff"/><path d="M6 11.5l3.5 3.5L16 8" fill="none" stroke="#ff6d00" stroke-width="2.6" stroke-linecap="round" stroke-linejoin="round"/></svg>
      <span>We walk in your shoes. We’ve been on the other side of the recruitment process - your side (wether you’re a talent or an employer),</span>
    </div>
    <p class="why-call">Call us on 0207 555 0184 or say “hello” at info@brisktalent.com</p>
  </section>

  <footer class="site-footer">
    <p class="legal">© 2017 Company Name&nbsp; All right reserved&nbsp; Term of Use</p>
    <ul class="social">
      <li></li><li></li><li></li><li></li>
    </ul>
  </footer>
</div>
</body>
</html>
```